Marketing Collaterals
Flyer, edm, web template, product label, brochure, vouchers
Hi Brondel,
Thanks for your new submissions. I like the look and feel of this set of collaterals. But as mentioned, no need to work on flyer and label.
And pls make the voucher generic so I can stamp the value of the voucher on it. Pls also make the voucher simpler and cleaner looking.
Thanks
HI Everyone,
Just to reiterate:
No need to work on flyer, product label, edm anymore.
Only need to work on the following in order of priority:
1) Website
2) Vouchers (1 generic version that I can rubber stamp value of voucher on it) pls take note of size - 148.5 mm x 70 mm
3) Brochure
Thanks.
Hi everyone,
I also noticed many of you used a lot of curves and wavy lines. I much prefer simple, clean cut straight lines. With a zen feel.
The closest to it now is probably #25.
The offer posters that I uploaded as well as the stock images should give you a clear idea of what I'm looking for.
Thanks again.
I also noticed that many of you used images that are not quite suitable. Either because they are too feminine, or contradicts the services we provide. Eg. our upper body massages are provided on chairs, so images of people lying on their back while receiving a massage may be misleading.
To make it easier for all, I have gone to Pixelharbor to look for suitable images. Here is the link to my lightbox http://www.pixelharbor-example.com/public_lightbox.mhtml?lightbox_id=48207615&code=3ac19b8e2d4470fa61c8e3907b15d2c4
Pls limit images to those in the light box instead.
Pls let me know if the link to the lightbox is not working.
Hi Everyone,
Hope you had a great start to the new year.
I am sorry for keeping all of you waiting. My business start up is going through some teething problems that prevented me from devoting time to work on the marketing collaterals. Thank you all for your patience and understanding.
And I thank the staff @ Plenvarta for allowing me to reopen this project.
To keep the project more focussed and simpler, I have decided to drop several of the items in the original scope of work, leaving only 3 items. Pls see below for update:
Items to work on in order of priority:
1)Website template
- I have uploaded an updated copy for the website
- Look and feel should be simple, clean and sophisticated
- Main colour will be black
- I have uploaded my business card, the label for the Dead Sea Salt packaging as well as 2 offer posters for your reference so you know what kind of look I am going for
2) Gift Vouchers
- Dimensions: 148.5 mm x 70 mm
- 4 colour x 1 colour
- back of the voucher will feature terms and conditions
- To save on print cost, I would like to have one single version of the voucher, with the flexibility to rubber stamp the value of the voucher. (pls let me know if this is not clear and I will be happy to clarify what I mean)
- Voucher value could include: $5 spa cash, $50 spa cash, 40 mins Foot Reflexology, 20 mins Upper Body Massage etc. These values will be rubber stamped prominently onto the generic voucher.
- Dimension: Open size - 210mm x 297mm
Closed size - 210mm x 99mm
- Brochure should follow the look and feel of the website
- Copy will need to be cut back quite a bit
Hope this provides clearer direction now.
Thank you and I look forward to seeing your work.
Hi to all designers who submitted your designs. I have been very bogged down by a series of unexpected issues on the business front. Hence have not devote time to work on this. Will look into this as soon as I can.
To staff of plenvarta, i understand I would normally have 7 days to decide but I need more time. I will come back as soon as I can.
Thanks to all for understanding.
Thanks to all designers who submitted your designs. Apologies for not getting back and providing feedback on your designs as I have been very busy with the opening of the shop.
Am looking through all of your work now. Will come back soon.
kindly send feedback on the above entries. thanks
Working on it :)
Dear Project Holder,
I saw your project.I am working on it.thanks.
Hi NimbusForgeArt,
Thank you for your submission.
Here are my comments:
#1 - As mentioned, the images of the ladies are not very appropriate and does not align with the offerings and image of the place we want to portray.
#2 - Same comments on the images of the ladies. Also, one side of the flyer should introduce Kelp Arbor and it's services and the other side is purely on the offers.
#3 - Many of images used are again not suitable as they are not part of our service offering and some of the fish therapy pictures feature the wrong type of fish.
Tip: Keep the creatives clean. Maybe better to have few but bigger appropriate pictures then to have many small pictures.
Hope the comments are helpful.
Thank you.
Hi Rovantoad,
I had every intention to award the job at the end. But if it makes it more secure, I have now guaranteed the job. I have also increased the prize money from $400 previously to $800 now.
Thanks for the feedback and hope to see your submission.
Hi all,
I need to add one more item:
Promotional pull up banner standee
It will feature the 2 promotional offers as stated in the flyer.
Also, pls note that for the A5 flyer, my preference is for it to be portrait rather than landscape.
Dear 7pixelcrafter and Brondel,
Thanks for your feedback. I have increased the prize money.
Hope to see your work soon.

```html
<!DOCTYPE html>
<html lang="en">
<head>
<meta charset="utf-8">
<title>Kelp Arbor – Foot Reflexology and Fish Spa</title>
<link rel="stylesheet" href="https://fonts.googleapis.com/css2?family=Arimo:wght@400;700&family=Lora:ital,wght@1,400&display=swap">
<style>
:root{
  --bg:#000;
  --text:#d8d8d8;
  --muted:#a9a9a9;
  --white:#fff;
  --blue:#33b6e8;
  --green:#9ccf2e;
  --hero-bg:#fbfbfb;
  --hero-text:#1a1a1a;
  --title:#555;
  --divider:#3a3a3a;
}
*{margin:0;padding:0;box-sizing:border-box}
html,body{width:1200px;height:1077px;overflow:hidden;background:var(--bg)}
body{font-family:"Arimo",Arial,sans-serif;color:var(--text);position:relative}
a{color:inherit;text-decoration:none}

.site-header{position:absolute;left:0;top:0;width:1200px;height:258px;background:linear-gradient(#101010,#000)}
.brand{position:absolute;left:44px;top:40px;width:250px}
.brand-mark{width:78px;height:78px;border-radius:50%;background:var(--blue);margin-left:40px;margin-bottom:8px}
.brand-name{font-size:42px;color:var(--blue);font-weight:400;line-height:1}
.brand-tagline{font-size:15px;color:var(--green);margin-top:6px}
.main-nav{position:absolute;left:322px;top:96px;display:flex;font-size:15px;font-weight:700;color:var(--blue)}
.main-nav a{padding:0 16px;border-left:2px solid var(--blue);line-height:16px}
.main-nav a:first-child{border-left:none;padding-left:0}
.nav-rule{position:absolute;left:322px;top:128px;width:853px;height:1px;background:#1d3b4a}

.hero{position:absolute;left:0;top:258px;width:1200px;height:287px;background:var(--hero-bg);border-bottom:5px solid var(--green)}
.hero-photo{position:absolute;left:0;top:0;width:630px;height:282px;background:linear-gradient(120deg,#d8b39a 0%,#f2e6e8 40%,#7d6a73 70%,#e9d9e6 100%)}
.hero-title{position:absolute;left:640px;top:52px;white-space:nowrap;font-family:"Lora",Georgia,serif;font-style:italic;font-size:46px;line-height:1.1;color:var(--title)}
.hero-lead{position:absolute;left:662px;top:138px;width:470px;font-size:17px;font-weight:700;color:var(--hero-text);line-height:1.3}
.hero-copy{position:absolute;left:662px;top:200px;width:480px;font-size:14px;color:#333;line-height:1.45}

.content{position:absolute;left:0;top:550px;width:1200px;height:385px}
.col{position:absolute;top:0;height:385px}
.col-products{left:59px;width:350px}
.col-services{left:460px;width:390px}
.col-news{left:930px;width:245px}
.divider{position:absolute;top:10px;width:2px;height:370px;background:var(--divider)}
.col h2{font-size:19px;font-weight:700;color:var(--green);margin-top:10px;margin-bottom:30px;text-transform:uppercase}
.item{display:flex;gap:18px;margin-bottom:22px}
.thumb{flex:none;width:88px;height:92px;background:linear-gradient(#eee,#777);border-radius:2px}
.col-services .thumb{width:132px;height:80px;background:linear-gradient(135deg,#e9d2bd,#b08a74)}
.col-services .item:nth-child(3) .thumb{background:linear-gradient(135deg,#2a2a2a,#c98aa7)}
.item h3{font-size:19px;font-weight:700;color:var(--blue);margin-bottom:6px}
.item p{font-size:14px;line-height:1.3;color:var(--muted)}
.item p span{color:var(--white)}
.more-link{display:block;margin-left:106px;font-size:19px;font-weight:700;color:var(--blue)}
.news h3{font-size:19px;font-weight:700;color:var(--blue);margin-bottom:6px}
.news p{font-size:14px;line-height:1.3;color:var(--muted);margin-bottom:26px}

.site-footer{position:absolute;left:0;top:945px;width:1200px;height:132px;background:linear-gradient(#2a2a2a,#0c0c0c 60%,#000);border-top:4px solid #1f6c8c}
.footer-nav{position:absolute;top:50px;width:1200px;text-align:center;font-size:15px;color:var(--blue)}
.footer-nav a{padding:0 6px;border-left:1px solid var(--blue)}
.footer-nav a:first-child{border-left:none}
.copyright{position:absolute;top:86px;width:1200px;text-align:center;font-size:15px;color:var(--blue)}
</style>
</head>
<body>
<header class="site-header">
  <div class="brand">
    <div class="brand-mark"></div>
    <div class="brand-name">Kelp Arbor</div>
    <div class="brand-tagline">Foot Reflexology and Fish Spa</div>
  </div>
  <nav class="main-nav">
    <a href="#">HOME</a><a href="#">SERVICES</a><a href="#">PRODUCTS</a><a href="#">MEMBERSHIP AND VOUCHERS</a><a href="#">PROMOTION</a><a href="#">OUTLET LOCATION</a>
  </nav>
  <div class="nav-rule"></div>
</header>

<section class="hero">
  <div class="hero-photo" role="img" aria-label="Feet resting beside a bowl of water with pink orchids and spa stones"></div>
  <div class="hero-title">Welcome to our Web Site !</div>
  <p class="hero-lead">Ea consetetur sadi consetetur sadi pscing lorem ipsum dolor lorem ipsum dolor sed amet</p>
  <p class="hero-copy">Consetetur pscing elitr, sed diam nonumy eirmod Erat, sed diam voluptua. Dolores et ex consetetur sadi pscing elitr | details</p>
</section>

<main class="content">
  <section class="col col-products">
    <h2>Featured Products</h2>
    <div class="item">
      <div class="thumb" role="img" aria-label="Jar of spa salt product"></div>
      <div><h3>Consetetur sadi</h3><p>consetetur pscing elitr, sed diam nonumy lorem ipsum dolor | <span>details</span></p></div>
    </div>
    <div class="item">
      <div class="thumb" role="img" aria-label="Silver cosmetic tub"></div>
      <div><h3>Lorem ipsum sadi</h3><p>consetetur pscing elitr, sed diam nonumy lorem ipsum dolor | <span>details</span></p></div>
    </div>
    <a class="more-link" href="#">more products</a>
  </section>
  <div class="divider" style="left:434px"></div>

  <section class="col col-services">
    <h2>Our Services</h2>
    <div class="item">
      <div class="thumb" role="img" aria-label="Foot reflexology treatment"></div>
      <div><h3>Foot Reflexology</h3><p>consetetur pscing elitr, sed diam nonumy lorem ipsum dolor lorem ipsum</p></div>
    </div>
    <div class="item">
      <div class="thumb" role="img" aria-label="Seated upper body massage"></div>
      <div><h3>Upper Body Massage</h3><p>Dolores et ex consetetur sadi pscing elitr nonumy lorem ipsum</p></div>
    </div>
    <div class="item">
      <div class="thumb" role="img" aria-label="Feet in a fish spa bowl with orchids"></div>
      <div><h3>Fish Spa</h3><p>Consetetur pscing elitr, sed eirmod Erat, sed diam volupt Dolores et ex consetetur sadi</p></div>
    </div>
  </section>
  <div class="divider" style="left:871px"></div>

  <section class="col col-news news">
    <h2>News &amp; Events</h2>
    <h3>Consetetur sadi</h3>
    <p>consetetur pscing elitr, sed diam nonumy lorem ipsum dolor</p>
    <h3>Lorem consetetur</h3>
    <p>Dolores et ex consetetur sadi pscing elitr nonumy lorem ipsum</p>
  </section>
</main>

<footer class="site-footer">
  <nav class="footer-nav">
    <a href="#">Home</a><a href="#">About us</a><a href="#">Services</a><a href="#">Products</a><a href="#">News &amp; Events</a><a href="#">Contacts</a>
  </nav>
  <p class="copyright">Copyright © Your Company Name</p>
</footer>
</body>
</html>
```